Swim school needs flyer design

Need revamp of flyer design. Attached last years flyer (BCP A4 Holiday Leaflet-v6.2 (1)). Also attached is this years information in word format (BCP A4 BCP & Holiday Leaflet 2014-2015).
This flyer must fit with our logo (Blue Current Pools-RGB). This flyer is our first point of call for many of our clients. With the amount of information that must be provided, it is important that it flows and is appealing. Photos can be accessed from http://kemapics.brightfolio.net/apps/photos/album?albumid=52930417 or from your own source
Important that the final design fits printers template.(Flyers-A4-210x297mm-2Side - attached)

```html
<!DOCTYPE html>
<html lang="en">
<head>
<meta charset="utf-8">
<title>Blue Current Pools – Term Dates &amp; Prices</title>
<link rel="stylesheet" href="https://fonts.googleapis.com/css2?family=Open+Sans:ital,wght@0,400;0,600;0,700;1,400;1,600;1,700;1,800&display=swap">
<style>
  :root{
    --orange:#f0931f;
    --green:#bfd232;
    --blue:#14a9d6;
    --panel:rgba(250,250,232,0.72);
    --ink:#1d1d1b;
    --white:#ffffff;
    --page:#e8e5e1;
  }
  *{margin:0;padding:0;box-sizing:border-box}
  html,body{width:1040px;height:1200px;overflow:hidden;background:var(--page)}
  body{font-family:"Open Sans",Arial,sans-serif;color:var(--ink)}
  .flyer{position:absolute;left:70px;top:19px;width:900px;height:1162px;background:var(--white);overflow:hidden;box-shadow:0 6px 24px rgba(0,0,0,.18)}
  .flyer-bg{position:absolute;inset:0}
  .headline{position:absolute;left:60px;top:28px;color:var(--white);font-style:italic;font-weight:700;line-height:1}
  .headline h1{font-size:56px;font-weight:700;letter-spacing:.5px}
  .headline p{font-size:28px;font-weight:700;margin-top:10px;margin-left:-4px}
  .term-panel{position:absolute;left:11px;top:200px;width:298px;height:623px;background:var(--panel)}
  .term{position:absolute;left:22px;font-style:italic;font-weight:700;font-size:15px;line-height:1.2}
  .term .booking{font-size:13.5px}
  .prices{border-collapse:collapse;margin-top:8px;margin-left:2px}
  .prices td{background:var(--orange);color:var(--white);border:1.5px solid var(--white);width:62px;height:27px;text-align:center;font-size:12.5px;font-weight:600;font-style:italic}
  .note{position:absolute;left:24px;top:556px;width:240px;font-size:11px;font-style:italic;font-weight:700;line-height:1.2}
  .call-badge{position:absolute;left:592px;top:152px;width:284px;height:284px;border-radius:50%;background:var(--blue);border:7px solid var(--white);color:var(--white);text-align:center;font-style:italic;transform:rotate(4deg);padding-top:54px}
  .call-badge .cta{font-size:42px;font-weight:700;line-height:1}
  .call-badge .phone{font-size:48px;font-weight:700;line-height:1.15}
  .call-badge .limit{font-size:17px;font-weight:700;margin-top:8px}
  .classes{position:absolute;left:503px;top:562px;color:var(--white);font-style:italic}
  .classes li{list-style:none;margin-bottom:17px}
  .classes h2{font-size:25px;font-weight:700;line-height:1.1}
  .classes span{font-size:18px;font-weight:600}
  .web{position:absolute;left:44px;top:870px;color:var(--white);font-size:51px;font-weight:700;font-style:italic;transform:rotate(-1.3deg);letter-spacing:.3px}
  .important{position:absolute;left:22px;top:975px;width:600px;font-style:italic}
  .important h3{font-size:25px;font-weight:700;margin-left:2px}
  .important ul{list-style:none;margin-top:4px}
  .important li{font-size:13px;font-weight:600;line-height:1.32}
  .important li::before{content:"• "}
  .brand{position:absolute;left:660px;top:1075px;display:flex;align-items:center;gap:10px}
  .brand-dot{width:26px;height:26px;border-radius:50%;background:var(--orange)}
  .brand-name{font-size:26px;font-weight:600;color:var(--blue)}
</style>
</head>
<body>
<div class="flyer">
  <svg class="flyer-bg" width="900" height="1162" viewBox="0 0 900 1162" aria-hidden="false">
    <defs>
      <linearGradient id="water" x1="0" y1="0" x2="1" y2="1">
        <stop offset="0" stop-color="#9fd3e4"/>
        <stop offset=".5" stop-color="#cfe8ee"/>
        <stop offset="1" stop-color="#8cc6da"/>
      </linearGradient>
    </defs>
    <g role="img" aria-label="Photograph of a baby swimming underwater, held by an adult's hands">
      <rect x="0" y="120" width="900" height="470" fill="url(#water)"/>
    </g>
    <path d="M0 0H900V140Q620 118 330 150Q150 168 0 170Z" fill="var(--orange)"/>
    <path d="M0 170Q150 168 330 150Q620 118 900 140" fill="none" stroke="var(--white)" stroke-width="6"/>
    <path d="M0 560Q280 518 560 534Q760 546 900 520V880H0Z" fill="var(--green)"/>
    <path d="M0 560Q280 518 560 534Q760 546 900 520" fill="none" stroke="var(--white)" stroke-width="6"/>
    <path d="M0 866L900 840V945L0 960Z" fill="var(--blue)"/>
    <path d="M0 862L900 836" stroke="var(--white)" stroke-width="6"/>
  </svg>

  <header class="headline">
    <h1>Blue Current Pools Classes</h1>
    <p>2013/14 Term Dates &amp; Prices</p>
  </header>

  <section class="term-panel">
    <div class="term" style="top:20px">
      *2014: Term 4 – 10 week term<br>Oct 6th – Dec 14th<br><span class="booking">Bookings taken from 22nd Sep 2014</span>
      <table class="prices"><tr><td>Babies</td><td>Transition</td><td>BCP</td><td>TSG</td></tr><tr><td>$155</td><td>$165</td><td>$170</td><td>$210</td></tr></table>
    </div>
    <div class="term" style="top:155px">
      *2015: Term 1 – 9 week term<br>Jan 27th – Mar 29th<br><span class="booking">Bookings taken from 15th Dec 2014</span>
      <table class="prices"><tr><td>Babies</td><td>Transition</td><td>BCP</td><td>TSG</td></tr><tr><td>$139.5</td><td>$148.5</td><td>$153</td><td>$189</td></tr></table>
    </div>
    <div class="term" style="top:290px">
      *2015: Term 2 – 11 week term<br>Apr 13th – Jun 28th<br><span class="booking">Bookings taken from 30th Mar 2015</span>
      <table class="prices"><tr><td>Babies</td><td>Transition</td><td>BCP</td><td>TSG</td></tr><tr><td>$170</td><td>$176</td><td>$181.5</td><td>$231</td></tr></table>
    </div>
    <div class="term" style="top:425px">
      2015: Term 3 – 10 week term<br>Jul 13th – Sep 20th<br><span class="booking">Bookings taken from 29th Jun 2015</span>
      <table class="prices"><tr><td>Babies</td><td>Transition</td><td>BCP</td><td>TSG</td></tr><tr><td>$160</td><td>$170</td><td>$175</td><td>$215</td></tr></table>
    </div>
    <p class="note">* Note that these terms have public holidays and prices will be adjusted accordingly.</p>
  </section>

  <div class="call-badge">
    <div class="cta">Call now!</div>
    <div class="phone">9312 4470</div>
    <div class="limit">Limited places only..</div>
  </div>

  <ul class="classes">
    <li><h2>Baby Awareness</h2><span>½ hour class per week</span></li>
    <li><h2>Baby Transition Classes</h2><span>½ hour class per week</span></li>
    <li><h2>Blue Current Pools Classes</h2><span>½ hour class per week</span></li>
    <li><h2>Transitional Stroke Group</h2><span>1 hour class per week</span></li>
  </ul>

  <div class="web">www.bluecurrentpools.com.au</div>

  <section class="important">
    <h3>Important</h3>
    <ul>
      <li>No bookings are taken without a fully completed enrolment form and payment.</li>
      <li>Read BCPV Policies and Procedures for information on discounts, payment methods, refunds and makeups.</li>
      <li>Book early – place are limited due to small class sizes.</li>
      <li>Bookings can only be made in person at our Riverside Office or online.</li>
      <li>During holidays, all bookings must be done via the Riverside Office.</li>
      <li>Photographs and video footage is not allowed to be taken without the permission of all the parents/ guardians whose children are in the class.</li>
    </ul>
  </section>

  <div class="brand">
    <span class="brand-dot"></span>
    <span class="brand-name">Blue Current Pools</span>
  </div>
</div>
</body>
</html>
```